Hi,

I would like to have a invitation made for a party. exactly like the picture in the link below.

http://pinboardia.example/pin/529174603381046725/

However, Please change the colors into fun/ girly feeling. font can be different and size of the card should be the same

Name of the girl: RUBA
What: Bachelorette Party
Where:TIKO Boat
Dubai Coral Sails Club
When:7th of February 2013

No RSVP required. (so no need to put it)

```html
<!DOCTYPE html>
<html lang="en">
<head>
<meta charset="utf-8">
<title>Ruba's Bachelorette Party Invitation</title>
<link rel="stylesheet" href="https://fonts.googleapis.com/css2?family=Rye&family=Federo&family=Holtwood+One+SC&family=Crimson+Text:wght@400&display=swap">
<style>
  :root {
    --backdrop: #3a3a3c;
    --paper: #f7f1dd;
    --paper-fold: #efe7d1;
    --paper-back: #ebe3cb;
    --purple: #5b2e86;
    --pink: #d8336e;
    --pink-deep: #a51f52;
    --ornament: #7d57a3;
  }
  * { margin: 0; padding: 0; box-sizing: border-box; }
  html, body {
    width: 1200px;
    height: 900px;
    overflow: hidden;
    background: var(--backdrop);
  }
  .invitation {
    position: absolute;
    left: 85px;
    top: 205px;
    width: 1030px;
    height: 489px;
    display: flex;
    box-shadow: 0 6px 18px rgba(0,0,0,0.35);
  }
  .panel { position: relative; height: 100%; width: 343.4px; }
  .panel--front { background: var(--paper); }
  .panel--middle { background: linear-gradient(90deg, var(--paper-fold), var(--paper) 60%); }
  .panel--details { background: linear-gradient(90deg, var(--paper-back), var(--paper-fold)); }

  .headline {
    position: absolute;
    left: 0; top: 0;
    width: 1030px; height: 489px;
    pointer-events: none;
  }
  .headline__name { font-family: "Rye", serif; fill: var(--purple); }
  .headline__tagline { font-family: "Federo", sans-serif; fill: var(--purple); }
  .headline__single { font-family: "Rye", serif; fill: var(--pink); }
  .headline__single-depth { font-family: "Rye", serif; fill: var(--pink-deep); }
  .divider-line { stroke: var(--purple); stroke-width: 2; }
  .divider-tip { fill: var(--purple); }
  .ornament { fill: var(--ornament); opacity: 0.35; }

  .details-frame {
    position: absolute;
    left: 714px; top: 29px;
    width: 288px; height: 430px;
    pointer-events: none;
  }
  .details {
    position: absolute;
    left: 714px; top: 29px;
    width: 288px; height: 430px;
    text-align: center;
  }
  .details__label, .details__value, .details__note {
    position: absolute;
    left: 0; width: 100%;
    line-height: 1;
  }
  .details__label {
    font-family: "Holtwood One SC", serif;
    font-size: 12px;
    letter-spacing: 1px;
    color: var(--purple);
  }
  .details__value {
    font-family: "Crimson Text", serif;
    font-size: 16px;
    color: var(--pink);
  }
  .details__note {
    font-family: "Crimson Text", serif;
    font-size: 12px;
    color: var(--pink);
  }
</style>
</head>
<body>
  <main class="invitation">
    <section class="panel panel--front"></section>
    <section class="panel panel--middle"></section>
    <section class="panel panel--details"></section>

    <svg class="headline" viewBox="0 0 1030 489" aria-label="Ruba's last chance to celebrate being single">
      <rect class="ornament" x="263" y="10" width="73" height="72" rx="8" role="img" aria-label="Swirling corner flourish ornament"/>
      <rect class="ornament" x="9" y="405" width="70" height="72" rx="8" role="img" aria-label="Swirling corner flourish ornament"/>

      <text class="headline__name" x="17" y="170" font-size="92" textLength="317" lengthAdjust="spacingAndGlyphs">RUBA’S</text>

      <line class="divider-line" x1="358" y1="154" x2="480" y2="154"/>
      <line class="divider-line" x1="555" y1="154" x2="670" y2="154"/>
      <polygon class="divider-tip" points="352,154 364,150 364,158"/>
      <polygon class="divider-tip" points="676,154 664,150 664,158"/>
      <rect class="ornament" x="486" y="130" width="63" height="38" rx="6" role="img" aria-label="Scrolled center flourish ornament"/>

      <text class="headline__tagline" x="16" y="228" font-size="64" textLength="662" lengthAdjust="spacingAndGlyphs">LAST CHANCE TO CELEBRATE BEING</text>

      <text class="headline__single-depth" x="21" y="373" font-size="168" textLength="660" lengthAdjust="spacingAndGlyphs">SINGLE</text>
      <text class="headline__single" x="15" y="368" font-size="168" textLength="660" lengthAdjust="spacingAndGlyphs">SINGLE</text>
    </svg>

    <svg class="details-frame" viewBox="0 0 288 430" aria-hidden="true">
      <rect x="1" y="1" width="286" height="428" rx="40" fill="none" stroke="var(--purple)" stroke-width="2"/>
      <rect x="6" y="6" width="276" height="418" rx="35" fill="none" stroke="var(--purple)" stroke-width="2" stroke-dasharray="1 3"/>
      <rect x="10" y="10" width="268" height="410" rx="31" fill="none" stroke="var(--purple)" stroke-width="1.5"/>
      <line x1="104" y1="391" x2="184" y2="391" stroke="var(--purple)" stroke-width="1.5"/>
      <polygon points="98,391 144,387.5 190,391 144,394.5" fill="var(--purple)"/>
    </svg>

    <div class="details">
      <p class="details__label" style="top:51px">WHO</p>
      <p class="details__value" style="top:75px">Ruba</p>

      <p class="details__label" style="top:128px">WHAT</p>
      <p class="details__value" style="top:150px">Bachelorette Party!</p>

      <p class="details__label" style="top:205px">WHEN</p>
      <p class="details__note" style="top:227px">the evening of</p>
      <p class="details__value" style="top:240px">February 7, 2013</p>

      <p class="details__label" style="top:292px">WHERE</p>
      <p class="details__value" style="top:312px">TIKO Boat</p>
      <p class="details__note" style="top:333px">Dubai Coral Sails Club</p>
    </div>
  </main>
</body>
</html>
```